Neu Online platform and Web design for Professional Car Trade. LORVANTIQ

Web design for Professional Car Trade. www.lorvantiq.example European car dealer, trader, import, premium and classic cars, Campervans and trucks. The online platform must be modern, clean and very classy. We are agents that advise and help import vehicles from Europe. DESCRIPTION: We are professionals of the Import of Vehicles in Europe that need an informative Web page of their services. Under the Lorvantiq brand We help people to find their ideal car in the European market, mainly Germany. Completely revised and with official guarantee. Service with personalized attention and advice to the client since he chooses his first vehicle, search and delivery. Key on hand. We are dedicated to advising, managing and importing vehicles from different countries of the European Union for clients from all over the country. Our company is at your service in everything related to Import of vehicles. If you need any clarification about our services or our way of working, you can contact us by email by sending it to the following address: Info@lorvantiq.example where we will assist you and give you all the necessary information and try to clear all your doubts. We have different services tailored and adapted to the needs of our customers. 100% professional and carefree service, tell us what car you want and we take care of everything. Help with documentation and calculation of taxes, registration tax, circulation, ITV, traffic. Budget without commitment, simulation of all costs and final prices in Spain. We speak the language in origin We have a qualified professional team for the valuation and documentation of the vehicles that are needed. Approvals, reforms, small cards, historical .. etc Website in German, English and Spanish Examples / Examples: https://www.trasvelmotor.example/ https: // www. ruzelpick.example.uk/brenta www.ruzelpick.example.de http://motvelora.example Info: http://www.ruedapress.example/practicos/comprar-coche-alemania http://www.vehitrasa.example/residencia. php http://importacionesolmedaz.example/cotizaciones.php
Reason: I have not received the expected designs I have not received more designs as expected
Target Market(s)
Sale of import and export vehicles for the Spanish and German automobile market.
Industry/Entity Type
Automotive
Logo Text
LORVANTIQ
Number of Pages Required
5+ page
Requirements
Nice to have
- I have some idea how in a background put a nice picture of some classic vehicle.

```html
<!DOCTYPE html>
<html lang="en">
<head>
<meta charset="utf-8">
<title>Lorvantiq – European Car Import</title>
<link href="https://fonts.googleapis.com/css2?family=Raleway:wght@400;500;600;700;800&family=Open+Sans:wght@400;600;700&display=swap" rel="stylesheet">
<style>
:root{
  --orange:#f07f1e;
  --blue:#1e8fd0;
  --blue-band:#2a8ecb;
  --green:#9cc63b;
  --ink:#222;
  --text:#555;
  --muted:#888;
  --line:#dcdcdc;
  --soft:#f3f3f3;
  --white:#fff;
}
*{box-sizing:border-box;margin:0;padding:0}
html,body{width:1200px;height:3947px;overflow:hidden}
body{position:relative;background:var(--white);font-family:"Open Sans",Arial,sans-serif;color:var(--text);font-size:14px}
.abs{position:absolute}
h1,h2,h3,.raleway{font-family:"Raleway",Arial,sans-serif}

/* header */
.site-header{position:absolute;left:0;top:0;width:1200px;height:92px;background:var(--white);border-top:4px solid var(--blue)}
.brand{position:absolute;left:97px;top:28px;font-family:"Raleway",sans-serif;font-size:30px;font-weight:600;color:var(--blue)}
.topbar{position:absolute;right:97px;top:14px;font-size:13px;color:var(--ink);display:flex;gap:14px;align-items:center}
.topbar b{font-weight:700;font-style:italic}
.topbar .ico{color:var(--orange);margin-right:5px}
.nav{position:absolute;right:97px;top:58px;display:flex;gap:30px;font-family:"Raleway",sans-serif;font-size:15px;font-weight:600;color:var(--ink)}
.nav .active{color:var(--orange)}

/* hero */
.hero{position:absolute;left:0;top:92px;width:1200px;height:520px;overflow:hidden}
.hero-photo{position:absolute;inset:0;background:linear-gradient(100deg,#4c5053 0%,#7b7d78 35%,#cfc7bd 60%,#e8e6e2 78%,#9ea3a6 100%)}
.hero-title{position:absolute;left:97px;top:120px;font-family:"Raleway",sans-serif;font-size:48px;color:var(--white);letter-spacing:1px}
.hero-title b{font-weight:800}
.hero-title span{font-weight:400}
.hero-lead{position:absolute;left:97px;top:198px;width:520px;color:var(--white);font-size:18px;line-height:35px;font-weight:600}
.btn{display:inline-block;font-family:"Raleway",sans-serif;font-weight:700;font-size:14px;text-transform:uppercase;letter-spacing:.5px;text-align:center}
.btn-orange{background:var(--orange);color:var(--white)}
.hero .btn-start{position:absolute;left:97px;top:295px;width:158px;height:47px;line-height:47px}
.hero .btn-more{position:absolute;left:266px;top:295px;width:179px;height:47px;line-height:43px;border:2px solid var(--white);color:var(--white)}
.hero-curve{position:absolute;left:0;bottom:0}
.dots{position:absolute;left:562px;top:455px;display:flex;gap:6px}
.dots i{width:12px;height:12px;border-radius:50%;border:2px solid #fff;display:block}
.dots i.on{background:#fff}

/* welcome */
.welcome h2{position:absolute;left:103px;top:712px;font-size:32px;font-weight:700;color:var(--ink)}
.welcome h2 span{font-weight:500}
.welcome p{position:absolute;left:103px;width:530px;font-size:14px;line-height:25px;color:var(--text)}
.welcome .btn-read{position:absolute;left:103px;top:976px;width:130px;height:40px;line-height:36px;border:2px solid var(--line);color:var(--orange);font-size:13px}
.video{position:absolute;left:634px;top:715px;width:464px;height:305px;background:linear-gradient(120deg,#2b2520 0%,#5c4a3c 45%,#8d7a6b 70%,#3a3430 100%)}
.video .play{position:absolute;left:202px;top:122px}

/* steps */
.steps{position:absolute;left:0;top:1105px;width:1200px;height:436px;background:linear-gradient(#f1f1f1,#fafafa 40%,#fff)}
.section-title{position:absolute;left:0;width:1200px;text-align:center;font-family:"Raleway",sans-serif;font-size:32px;color:var(--ink)}
.section-title b{font-weight:700}
.section-title span{font-weight:500}
.step{position:absolute;top:150px;width:230px;text-align:center}
.step svg{display:block;margin:0 auto}
.step .num{margin-top:22px;font-family:"Raleway",sans-serif;font-weight:800;font-size:14px;color:var(--ink)}
.step .name{margin-top:14px;font-family:"Raleway",sans-serif;font-weight:600;font-size:17px;color:var(--blue)}
.step p{margin-top:12px;font-size:13px;line-height:21px;color:var(--muted)}
.chev{position:absolute;top:198px}

/* search */
.finder{position:absolute;left:0;top:1541px;width:1200px;height:752px;background:linear-gradient(135deg,#2d95d2,#2488c4 50%,#2d92cf)}
.finder .section-title{top:42px;color:var(--white)}
.vtype{position:absolute;left:97px;display:flex;align-items:center;gap:20px;color:var(--white);font-family:"Raleway",sans-serif;font-weight:800;font-size:14px}
.vtype .ring{width:92px;height:92px;border-radius:50%;border:4px solid var(--white);display:flex;align-items:center;justify-content:center}
.vtype.active .ring{background:var(--orange)}
.field{position:absolute;width:328px}
.field label{display:block;font-size:14px;color:var(--white);margin-bottom:7px}
.select,.input{height:38px;background:var(--white);border-radius:2px;position:relative}
.select{font-size:12px;color:#999;line-height:38px;padding-left:12px}
.select svg{position:absolute;right:12px;top:14px}
.field.wide{width:670px}
.consent{position:absolute;left:408px;top:629px;font-size:13px;color:var(--white);display:flex;align-items:center;gap:8px}
.consent i{width:13px;height:13px;background:var(--white);display:block}
.btn-search{position:absolute;left:408px;top:658px;width:210px;height:46px;line-height:46px}

/* services */
.plan{position:absolute;top:2454px;width:316px;height:452px;background:var(--white);border:1px solid var(--line);box-shadow:0 2px 5px rgba(0,0,0,.1);text-align:center}
.plan .head{height:45px;line-height:45px;color:var(--white);font-family:"Raleway",sans-serif;font-weight:700;font-size:18px}
.plan .price{height:91px;line-height:91px;background:var(--soft);font-family:"Open Sans",sans-serif;font-weight:700;font-size:40px;color:#333}
.plan .price small{font-size:14px;font-weight:400;color:#555;margin-left:6px}
.plan ul{list-style:none;margin-top:13px}
.plan li{font-size:13px;line-height:33px;color:var(--text)}
.plan li.two{line-height:20px;padding:6px 40px}
.plan li::before{content:"\2714";margin-right:8px;font-size:13px}
.plan .btn{position:absolute;left:50%;transform:translateX(-50%);top:380px;width:142px;height:46px;line-height:46px;color:var(--white)}
.basic .head,.basic .btn{background:var(--orange)} .basic li::before{color:var(--orange)}
.mid .head,.mid .btn{background:var(--blue)} .mid li::before{color:var(--blue)}
.prem .head,.prem .btn{background:var(--green)} .prem li::before{color:var(--green)}

/* payment */
.payment{position:absolute;left:0;top:2990px;width:1200px;height:390px;background:linear-gradient(100deg,#3a3b3d 0%,#6d6c6a 40%,#8a8784 60%,#4a4846 100%)}
.payment .section-title{top:56px;color:var(--white)}
.payment p{position:absolute;left:0;width:1200px;text-align:center;color:var(--white);font-size:16px;line-height:32px;font-weight:600}
.cards{position:absolute;left:480px;top:284px;display:flex;gap:10px}
.cards span{width:76px;height:46px;background:var(--white);border-radius:4px;display:flex;align-items:center;justify-content:center;font-family:"Open Sans",sans-serif;font-weight:700;font-size:14px;color:#777}

/* contact */
.col-title{position:absolute;font-family:"Raleway",sans-serif;font-weight:600;font-size:19px;color:var(--ink)}
.input{position:absolute;border:1px solid #ccc;font-size:12px;color:#888;padding:8px 12px}
.btn-submit{position:absolute;left:631px;top:3787px;width:95px;height:34px;line-height:34px;font-size:13px}
.info-row{position:absolute;left:781px;display:flex;gap:22px;align-items:center;font-size:12px;line-height:20px;color:var(--text)}
.info-row .pin{width:38px;height:38px;border-radius:50%;background:#eef3f7;display:flex;align-items:center;justify-content:center;flex:none}
.social{position:absolute;left:781px;top:3794px;display:flex;gap:8px}
.social i{width:30px;height:30px;border-radius:50%;display:block}
.footer-line{position:absolute;left:97px;top:3856px;width:1006px;height:1px;background:var(--line)}
.copyright{position:absolute;left:0;top:3890px;width:1200px;text-align:center;font-size:12px;color:var(--muted)}
.to-top{position:absolute;left:1074px;top:3880px}
</style>
</head>
<body>

<header class="site-header">
  <div class="brand">Lorvantiq</div>
  <div class="topbar">
    <span><span class="ico">&#9742;</span><b>1 888 888 8888</b></span><span>|</span>
    <span><span class="ico">&#10067;</span>Help</span><span>|</span>
    <span><span class="ico">&#9679;</span>Login</span>
  </div>
  <nav class="nav">
    <span class="active">Home</span><span>About</span><span>Importing</span><span>Buying advice</span><span>Services</span><span>Contact</span>
    <svg width="16" height="16" viewBox="0 0 16 16" style="margin-top:2px"><circle cx="6.5" cy="6.5" r="5" fill="none" stroke="#222" stroke-width="2"/><line x1="10" y1="10" x2="15" y2="15" stroke="#222" stroke-width="2.4"/></svg>
  </nav>
</header>

<section class="hero">
  <div class="hero-photo" role="img" aria-label="Smiling woman holding car keys beside a white car"></div>
  <h1 class="hero-title"><b>LORVANTIQ</b></h1>
  <p class="hero-lead">We are an European car dealer, trader, import, premium and classic cars, Campervans and trucks.</p>
  <span class="btn btn-orange btn-start">Get started</span>
  <span class="btn btn-more">Find out more</span>
  <div class="dots"><i class="on"></i><i></i><i></i><i></i></div>
  <svg class="hero-curve" width="1200" height="110" viewBox="0 0 1200 110" preserveAspectRatio="none"><path d="M0 40 Q600 150 1200 20 L1200 110 L0 110Z" fill="#fff"/></svg>
</section>

<section class="welcome">
  <h2>Welcome to <span>Lorvantiq</span></h2>
  <p style="top:770px">Te acompañamos y asesoramos en todo el proceso para que puedas disfrutar de tu coche en tu ciudad de origen listo para conducir.</p>
  <p style="top:845px">En Alemania elegimos varios modelos que te puedan interesar según tu criterio de búsqueda, motorización, color y equipamiento. Asegurándonos que el coche esta en perfecto estado y con toda la documentación en regla. s de 150.000 km en total.</p>
  <span class="btn btn-read">Read more</span>
  <div class="video" role="img" aria-label="Video still of a smiling man at the wheel of a car">
    <svg class="play" width="60" height="60" viewBox="0 0 60 60"><circle cx="30" cy="30" r="30" fill="#111"/><path d="M24 18 L42 30 L24 42Z" fill="#fff"/></svg>
  </div>
</section>

<section class="steps">
  <h2 class="section-title" style="top:58px"><b>How to</b> <span>buy a car</span></h2>
  <div class="step" style="left:88px">
    <svg width="60" height="60" viewBox="0 0 60 60" fill="none" stroke="#f07f1e" stroke-width="3.5"><rect x="5" y="8" width="50" height="34" rx="2"/><line x1="30" y1="42" x2="30" y2="52"/><line x1="18" y1="53" x2="42" y2="53"/></svg>
    <div class="num">STEP 1</div><div class="name">Choose the car</div>
    <p>At vero eos et accusamus et iusto<br>odio dig ni somos ducim.</p>
  </div>
  <div class="step" style="left:349px">
    <svg width="60" height="60" viewBox="0 0 60 60"><path d="M8 10 L30 8 L54 32 L32 54 L8 30Z" fill="#f07f1e"/><circle cx="19" cy="20" r="4" fill="#fff"/></svg>
    <div class="num">STEP 2</div><div class="name">Get offers</div>
    <p>At vero eos et accusamus et iusto<br>odio dig ni somos ducim.</p>
  </div>
  <div class="step" style="left:613px">
    <svg width="60" height="60" viewBox="0 0 60 60" fill="none" stroke="#f07f1e" stroke-width="4"><rect x="6" y="10" width="42" height="42" rx="3"/><path d="M16 30 L26 40 L54 8" stroke-width="5"/></svg>
    <div class="num">STEP 3</div><div class="name">Choose a plan</div>
    <p>At vero eos et accusamus et iusto<br>odio dig ni somos ducim.</p>
  </div>
  <div class="step" style="left:880px">
    <svg width="60" height="60" viewBox="0 0 60 60"><path d="M8 34 L14 18 Q16 14 20 14 L40 14 Q44 14 46 18 L52 34 L52 48 L8 48Z" fill="#f07f1e"/><rect x="16" y="20" width="28" height="10" fill="#fff"/><circle cx="16" cy="39" r="4" fill="#fff"/><circle cx="44" cy="39" r="4" fill="#fff"/><rect x="10" y="48" width="8" height="6" fill="#f07f1e"/><rect x="42" y="48" width="8" height="6" fill="#f07f1e"/></svg>
    <div class="num">STEP 4</div><div class="name">Buy the car</div>
    <p>At vero eos et accusamus et iusto<br>odio dig ni somos ducim.</p>
  </div>
  <svg class="chev" style="left:330px" width="36" height="24" viewBox="0 0 36 24" fill="none" stroke="#ccc" stroke-width="3"><path d="M4 3 L14 12 L4 21M18 3 L28 12 L18 21"/></svg>
  <svg class="chev" style="left:582px" width="36" height="24" viewBox="0 0 36 24" fill="none" stroke="#ccc" stroke-width="3"><path d="M4 3 L14 12 L4 21M18 3 L28 12 L18 21"/></svg>
  <svg class="chev" style="left:845px" width="36" height="24" viewBox="0 0 36 24" fill="none" stroke="#ccc" stroke-width="3"><path d="M4 3 L14 12 L4 21M18 3 L28 12 L18 21"/></svg>
</section>

<section class="finder">
  <h2 class="section-title"><b>Buy your car,</b> <span>which car do you prefer?</span></h2>

  <div class="vtype active" style="top:109px"><div class="ring"><svg width="54" height="30" viewBox="0 0 54 30"><path d="M3 20 L8 12 L18 10 L24 4 L38 4 L44 11 L51 13 L51 22 L3 22Z" fill="#fff"/><circle cx="14" cy="23" r="5" fill="#f07f1e" stroke="#fff" stroke-width="2"/><circle cx="40" cy="23" r="5" fill="#f07f1e" stroke="#fff" stroke-width="2"/></svg></div>CARS</div>
  <div class="vtype" style="top:235px"><div class="ring"><svg width="54" height="30" viewBox="0 0 54 30"><path d="M3 20 L6 13 L16 12 L22 5 L36 5 L42 12 L51 14 L51 22 L3 22Z" fill="#fff"/><circle cx="14" cy="23" r="5" fill="#2a8ecb" stroke="#fff" stroke-width="2"/><circle cx="40" cy="23" r="5" fill="#2a8ecb" stroke="#fff" stroke-width="2"/></svg></div>CLASSIC CARS</div>
  <div class="vtype" style="top:362px"><div class="ring"><svg width="54" height="32" viewBox="0 0 54 32"><path d="M3 4 L38 4 L48 14 L51 16 L51 24 L3 24Z" fill="#fff"/><circle cx="14" cy="25" r="5" fill="#2a8ecb" stroke="#fff" stroke-width="2"/><circle cx="40" cy="25" r="5" fill="#2a8ecb" stroke="#fff" stroke-width="2"/></svg></div>CAMPERVANS</div>
  <div class="vtype" style="top:488px"><div class="ring"><svg width="54" height="34" viewBox="0 0 54 34"><rect x="3" y="3" width="32" height="22" fill="#fff"/><path d="M37 10 L46 10 L51 18 L51 25 L37 25Z" fill="#fff"/><circle cx="13" cy="27" r="5" fill="#2a8ecb" stroke="#fff" stroke-width="2"/><circle cx="43" cy="27" r="5" fill="#2a8ecb" stroke="#fff" stroke-width="2"/></svg></div>TRUCKS</div>

  <div class="field" style="left:408px;top:118px"><label>Precio total (hasta)</label><div class="select">Indiferente<svg width="10" height="7" viewBox="0 0 10 7"><path d="M1 1 L5 5 L9 1" fill="none" stroke="#999" stroke-width="1.6"/></svg></div></div>
  <div class="field" style="left:755px;top:118px"><label>Cuota mensual financiado</label><div class="select">Indiferente<svg width="10" height="7" viewBox="0 0 10 7"><path d="M1 1 L5 5 L9 1" fill="none" stroke="#999" stroke-width="1.6"/></svg></div></div>
  <div class="field" style="left:408px;top:205px"><label>Marca</label><div class="select">Indiferente<svg width="10" height="7" viewBox="0 0 10 7"><path d="M1 1 L5 5 L9 1" fill="none" stroke="#999" stroke-width="1.6"/></svg></div></div>
  <div class="field" style="left:755px;top:205px"><label>Modelo</label><div class="select">Indiferente<svg width="10" height="7" viewBox="0 0 10 7"><path d="M1 1 L5 5 L9 1" fill="none" stroke="#999" stroke-width="1.6"/></svg></div></div>
  <div class="field" style="left:408px;top:292px"><label>Cambio</label><div class="select">Indiferente<svg width="10" height="7" viewBox="0 0 10 7"><path d="M1 1 L5 5 L9 1" fill="none" stroke="#999" stroke-width="1.6"/></svg></div></div>
  <div class="field" style="left:755px;top:292px"><label>Combustible</label><div class="select">Indiferente<svg width="10" height="7" viewBox="0 0 10 7"><path d="M1 1 L5 5 L9 1" fill="none" stroke="#999" stroke-width="1.6"/></svg></div></div>
  <div class="field" style="left:408px;top:379px"><label>Kilometros</label><div class="select">Indiferente<svg width="10" height="7" viewBox="0 0 10 7"><path d="M1 1 L5 5 L9 1" fill="none" stroke="#999" stroke-width="1.6"/></svg></div></div>
  <div class="field" style="left:755px;top:379px"><label>Años</label><div class="select">Indiferente<svg width="10" height="7" viewBox="0 0 10 7"><path d="M1 1 L5 5 L9 1" fill="none" stroke="#999" stroke-width="1.6"/></svg></div></div>
  <div class="field wide" style="left:408px;top:457px"><label>Nombre y apellidos(*)</label><div class="input" style="position:relative;border:none"></div></div>
  <div class="field" style="left:408px;top:536px"><label>Telefono (*)</label><div class="input" style="position:relative;border:none"></div></div>
  <div class="field" style="left:755px;top:536px"><label>Email(*)</label><div class="input" style="position:relative;border:none"></div></div>
  <div class="consent"><i></i>Tu privacidad nos importa. Acepta con tranquilidad las condiciones del servicio y la política de privacidad</div>
  <span class="btn btn-orange btn-search">Buscar mi doche</span>
</section>

<section class="services">
  <h2 class="section-title" style="top:2368px"><b>Our</b> <span>Services</span></h2>
  <div class="plan basic" style="left:97px">
    <div class="head">BASIC</div>
    <div class="price">XXX€<small>Per month</small></div>
    <ul>
      <li>Vuelta, compra y conduce. (fly and buy)</li>
      <li>Incluye negociación</li>
      <li>Asesoramiento</li>
      <li>Tramites</li>
      <li>Documentación</li>
      <li class="two">Ayuda con la reserva de vuelos y alojamiento</li>
    </ul>
    <span class="btn">Sign up now!</span>
  </div>
  <div class="plan mid" style="left:442px">
    <div class="head">INTERMEDIATE</div>
    <div class="price">XXX€<small>Per month</small></div>
    <ul>
      <li>Trust, buy and auto shipping*</li>
      <li>Coste total desde 1390 €</li>
      <li>Incluye negociación, asesoramiento</li>
      <li>Tramites de compra</li>
      <li>Documentación</li>
      <li>Preparación del envió.</li>
    </ul>
    <span class="btn">Sign up now!</span>
  </div>
  <div class="plan prem" style="left:784px">
    <div class="head">PREMIUM</div>
    <div class="price">XXX€<small>Per month</small></div>
    <ul>
      <li>Trust, buy and auto driving*</li>
      <li>Incluye negociación</li>
      <li>Asesoramiento</li>
      <li>Tramites de compra</li>
      <li>Documentación</li>
      <li>Seguro ( otros gastos aparte)</li>
    </ul>
    <span class="btn">Sign up now!</span>
  </div>
</section>

<section class="payment" role="img" aria-label="Hands typing on a laptop keyboard, darkened background">
  <h2 class="section-title"><b>Payment</b> <span>Options</span></h2>
  <p style="top:92px">At Lorvantiq you can make the payment by bank transfer. Or you can pay in cash<br>or by credit card directly at the branch.</p>
  <p style="top:184px">xxxxxxxxxxxxxxxx, Nordbank Halden, Deutschland (EUR) &nbsp; | &nbsp; IBAN: DExxxxxxx, SWIFT/BIC: xxxxxxxxx</p>
  <p style="top:218px">We accept all major credit cards:</p>
  <div class="cards"><span>Varda</span><span>Mestra</span><span>Paylo</span></div>
</section>

<section class="contact">
  <h2 class="section-title" style="top:3446px"><b>Contact</b> <span>Us</span></h2>
  <div class="col-title" style="left:97px;top:3532px">Contact form</div>
  <div class="input" style="left:97px;top:3598px;width:313px;height:34px">Name</div>
  <div class="input" style="left:418px;top:3598px;width:308px;height:34px">Phone No</div>
  <div class="input" style="left:97px;top:3642px;width:629px;height:34px">Email</div>
  <div class="input" style="left:97px;top:3687px;width:629px;height:82px">Message</div>
  <span class="btn btn-orange btn-submit">Submit</span>

  <div class="col-title" style="left:781px;top:3532px">Contact Information</div>
  <div class="info-row" style="top:3588px"><span class="pin"><svg width="12" height="16" viewBox="0 0 12 16"><path d="M6 1 A5 5 0 0 1 11 6 C11 10 6 15 6 15 C6 15 1 10 1 6 A5 5 0 0 1 6 1Z" fill="#2a8ecb"/><circle cx="6" cy="6" r="2" fill="#fff"/></svg></span><span>Level 1, Harlow Club,<br>48 Fenmore Street, Eastbrook</span></div>
  <div class="info-row" style="top:3652px"><span class="pin"><svg width="14" height="14" viewBox="0 0 14 14"><path d="M3 1 L5 4 L4 6 Q6 9 8 10 L10 9 L13 11 L11 13 Q5 13 1 5Z" fill="#2a8ecb"/></svg></span><span>1 888 888 8888</span></div>
  <div class="info-row" style="top:3713px"><span class="pin"><svg width="14" height="10" viewBox="0 0 14 10"><rect x="0.5" y="0.5" width="13" height="9" fill="none" stroke="#2a8ecb"/><path d="M1 1 L7 6 L13 1" fill="none" stroke="#2a8ecb"/></svg></span><span>info@lorvantiq.example</span></div>
  <div class="col-title" style="left:781px;top:3752px">Social Media</div>
  <div class="social"><i style="background:#3b5a9a"></i><i style="background:#2aa9e0"></i><i style="background:#0e76a8"></i><i style="background:#cb2027"></i></div>

  <div class="footer-line"></div>
  <div class="copyright">Copyright © 2017, Lorvantiq. All rights reserved.</div>
  <svg class="to-top" width="26" height="16" viewBox="0 0 26 16"><path d="M2 14 L13 3 L24 14" fill="none" stroke="#aaa" stroke-width="3"/></svg>
</section>

</body>
</html>
```